I need a graphic for the promotion email for our "8th Annual Brightwater Field Drills Academy" that incorporates our current logo and brand theme. I would like this graphic to funnel potentional attendees to register for a course. My perference would include a cool fire photo from our facility for the background. More information can be found on Kestrelvale.com and also our Facebook.

```html
<!DOCTYPE html>
<html lang="en">
<head>
<meta charset="utf-8">
<title>Brightwater Field Drills Academy – Email Banners</title>
<link rel="stylesheet" href="https://fonts.googleapis.com/css2?family=Montserrat:ital,wght@0,500;0,700;1,400;1,700;1,800;1,900&family=Teko:wght@600&display=swap">
<style>
  :root {
    --board: #b3b3b3;
    --night: #000000;
    --white: #ffffff;
    --ember: #ff5a1f;
    --flame-red: #e8130c;
    --flame-orange: #ff8a1c;
    --gold: #ffc21a;
    --steel: #f4f0ec;
    --hazard-yellow: #ffb400;
    --hazard-black: #151515;
    --button-red: #d41a1a;
    --button-deep: #a30d0d;
  }
  * { box-sizing: border-box; margin: 0; padding: 0; }
  html, body { width: 1108px; height: 1200px; overflow: hidden; }
  body { background: var(--board); position: relative; font-family: "Montserrat", sans-serif; }

  .banner {
    position: absolute; left: 198px; width: 710px; height: 474px;
    background: var(--night); overflow: hidden;
  }
  .banner--hose { top: 89px; }
  .banner--spray { top: 644px; }

  .hero-photo { position: absolute; }
  .banner--hose .hero-photo {
    left: 0; top: 0; width: 520px; height: 453px;
    background:
      radial-gradient(ellipse 22% 30% at 12% 55%, rgba(255,200,80,.95), transparent 70%),
      radial-gradient(ellipse 30% 42% at 15% 52%, rgba(255,120,20,.95), transparent 75%),
      radial-gradient(ellipse 18% 22% at 78% 62%, rgba(255,130,30,.85), transparent 75%),
      radial-gradient(ellipse 20% 35% at 85% 30%, rgba(190,70,15,.7), transparent 75%),
      radial-gradient(ellipse 26% 55% at 48% 60%, rgba(25,22,22,.95), transparent 70%),
      linear-gradient(180deg, #000 0%, #140704 18%, #3a1606 42%, #4a2a18 62%, #6d625b 78%, #8a8078 100%);
    -webkit-mask-image: linear-gradient(90deg, #000 72%, transparent 100%);
    mask-image: linear-gradient(90deg, #000 72%, transparent 100%);
  }
  .banner--spray .hero-photo {
    left: 0; top: 150px; width: 710px; height: 303px;
    background:
      radial-gradient(ellipse 16% 48% at 21% 58%, rgba(30,14,8,.95), transparent 72%),
      radial-gradient(ellipse 35% 25% at 45% 55%, rgba(255,190,120,.55), transparent 75%),
      radial-gradient(ellipse 45% 40% at 50% 80%, rgba(255,130,30,.9), transparent 75%),
      radial-gradient(ellipse 45% 35% at 95% 88%, rgba(255,190,60,.95), transparent 70%),
      radial-gradient(ellipse 30% 35% at 8% 85%, rgba(230,100,20,.85), transparent 75%),
      linear-gradient(180deg, #000 0%, #2a0e03 25%, #7a300a 60%, #c4601a 100%);
  }

  .brand {
    position: absolute; left: 38px; top: 120px; width: 210px;
    display: flex; align-items: center; justify-content: center; gap: 10px;
  }
  .brand__dot { width: 14px; height: 14px; border-radius: 50%; background: var(--ember); flex: none; }
  .brand__name {
    color: var(--white); font-weight: 500; font-size: 19px; letter-spacing: 3px;
  }

  .headline { position: absolute; left: 298px; top: 36px; width: 380px; font-style: italic; font-weight: 900; line-height: 1; }
  .headline__edition {
    display: block; font-size: 50px; letter-spacing: -1px;
    background: linear-gradient(180deg, var(--steel) 20%, #d59a6a 60%, var(--flame-orange) 100%);
    -webkit-background-clip: text; background-clip: text; color: transparent;
  }
  .headline__edition sup { font-size: 30px; vertical-align: 16px; }
  .headline__name {
    display: block; margin-top: 3px; font-size: 45px; letter-spacing: -1px;
    background: linear-gradient(100deg, var(--flame-red) 0%, var(--flame-orange) 40%, var(--flame-red) 70%, #ff3a10 100%);
    -webkit-background-clip: text; background-clip: text; color: transparent;
  }
  .headline__tag {
    display: block; margin-top: 6px; font-size: 22.5px; font-weight: 800;
    background: linear-gradient(90deg, var(--ember) 0%, var(--flame-orange) 40%, var(--gold) 100%);
    -webkit-background-clip: text; background-clip: text; color: transparent;
  }

  .divider {
    position: absolute; left: 296px; top: 173px; width: 376px; height: 1px;
    background: linear-gradient(90deg, rgba(255,255,255,.2), rgba(255,255,255,.8) 40%, rgba(255,255,255,.2));
  }
  .pitch {
    position: absolute; left: 298px; top: 195px; color: var(--white);
    font-style: italic; font-weight: 800; font-size: 15.4px; line-height: 22px;
  }

  .snapshot {
    position: absolute; top: 257px; width: 183px; height: 124px;
    border: 2px solid var(--white); box-shadow: 0 3px 8px rgba(0,0,0,.6);
  }
  .snapshot--drill { left: 297px; background: linear-gradient(160deg, #3b2b22 0%, #a5531e 35%, #6e6459 65%, #9a8f84 100%); }
  .snapshot--briefing { left: 490px; background: linear-gradient(180deg, #d8d6d0 0%, #9b9a95 40%, #4a5262 70%, #7c7a75 100%); }

  .cta {
    position: absolute; display: flex; align-items: center; justify-content: center;
    border: 2px solid var(--white); border-radius: 20px;
    background: linear-gradient(180deg, #f03a2e 0%, var(--button-red) 50%, var(--button-deep) 100%);
    color: var(--white); font-family: "Teko", sans-serif; font-weight: 600; letter-spacing: .5px;
    box-shadow: 0 2px 6px rgba(0,0,0,.5);
  }
  .banner--hose .cta { left: 524px; top: 392px; width: 148px; height: 33px; font-size: 22px; padding-top: 3px; }
  .banner--spray .cta { left: 304px; top: 398px; width: 177px; height: 39px; font-size: 26px; padding-top: 3px; }

  .seats { position: absolute; font-style: italic; font-weight: 400; }
  .banner--hose .seats { left: 534px; top: 430px; font-size: 11.2px; color: var(--white); }
  .banner--spray .seats { left: 496px; top: 410px; font-size: 13.2px; color: var(--hazard-black); }

  .hazard-band {
    position: absolute; left: 0; bottom: 0; width: 100%; height: 21px;
    background: repeating-linear-gradient(-60deg, var(--hazard-yellow) 0 11px, var(--hazard-black) 11px 22px);
  }
</style>
</head>
<body>

  <section class="banner banner--hose">
    <div class="hero-photo" role="img" aria-label="Firefighter in turnout gear advancing a hose line beside a large training fire"></div>
    <div class="brand"><span class="brand__dot"></span><span class="brand__name">KESTRELVALE</span></div>
    <h1 class="headline">
      <span class="headline__edition">8<sup>TH</sup> ANNUAL</span>
      <span class="headline__name">BRIGHTWATER</span>
      <span class="headline__tag">FIELD DRILLS ACADEMY</span>
    </h1>
    <div class="divider"></div>
    <p class="pitch">HANDS-ON EMERGENCY RESPONSE<br>TRAINING FOR INDUSTRY PROFESSIONALS</p>
    <div class="snapshot snapshot--drill" role="img" aria-label="Two trainees in gear working a live fire drill"></div>
    <div class="snapshot snapshot--briefing" role="img" aria-label="Group of attendees gathered for a field briefing"></div>
    <a class="cta">REGISTER NOW</a>
    <p class="seats">Limited Seats Available</p>
    <div class="hazard-band"></div>
  </section>

  <section class="banner banner--spray">
    <div class="hero-photo" role="img" aria-label="Firefighter with breathing apparatus spraying water into glowing orange flames"></div>
    <div class="brand"><span class="brand__dot"></span><span class="brand__name">KESTRELVALE</span></div>
    <h1 class="headline">
      <span class="headline__edition">8<sup>TH</sup> ANNUAL</span>
      <span class="headline__name">BRIGHTWATER</span>
      <span class="headline__tag">FIELD DRILLS ACADEMY</span>
    </h1>
    <div class="divider"></div>
    <p class="pitch">HANDS-ON EMERGENCY RESPONSE<br>TRAINING FOR INDUSTRY PROFESSIONALS</p>
    <div class="snapshot snapshot--drill" role="img" aria-label="Two trainees in gear working a live fire drill"></div>
    <div class="snapshot snapshot--briefing" role="img" aria-label="Group of attendees gathered for a field briefing"></div>
    <a class="cta">REGISTER NOW</a>
    <p class="seats">Limited Seats Available</p>
    <div class="hazard-band"></div>
  </section>

</body>
</html>
```